RW Frameworks Inc Business cards

We need business cards using our existing logo but slightly modified. Right now the logo says RW Framework Masonry. We want to keep the RW part of the design, but replace the Framework Masonry portion with "FRAMEWORKS". Please see the attached file.
Ideally this would be a blank template so we can add Different Names, titles, and phone numbers later.
On the one side we want only the logo and on the other side the detail. I'm attaching an example for you to see.
Please reach out with any other questions. Our address and other details will be given out once we find a design we like.

Target Market(s)

Construction Industry

```html
<!DOCTYPE html>
<html lang="en">
<head>
<meta charset="utf-8">
<title>RW Frameworks Inc — Business Cards</title>
<link rel="stylesheet" href="https://fonts.googleapis.com/css2?family=Arimo:wght@400;700&display=swap">
<style>
  :root {
    --page-bg: #d9dadc;
    --card-bg: #2c2c2e;
    --accent-blue: #1d83d4;
    --text-light: #c9cacc;
    --text-muted: #a6a7aa;
    --brand-grey: #b4b5b8;
  }
  * { box-sizing: border-box; margin: 0; padding: 0; }
  html, body {
    width: 1200px;
    height: 1200px;
    overflow: hidden;
    background: var(--page-bg);
    font-family: "Arimo", Arial, sans-serif;
  }
  .canvas {
    width: 1200px;
    height: 1200px;
    display: flex;
    flex-direction: column;
    align-items: center;
    justify-content: center;
    gap: 64px;
  }
  .card {
    position: relative;
    width: 900px;
    height: 514px;
    background: var(--card-bg);
    border-bottom: 12px solid var(--accent-blue);
    box-shadow: 0 10px 26px rgba(0, 0, 0, 0.22);
  }

  /* Back side: contact details */
  .contact-block {
    position: absolute;
    left: 270px;
    top: 180px;
    display: flex;
    align-items: center;
    gap: 26px;
  }
  .person { text-align: right; }
  .person-name {
    color: var(--accent-blue);
    font-weight: 700;
    font-size: 30px;
    letter-spacing: 0.5px;
  }
  .person-title {
    color: var(--text-light);
    font-size: 17px;
    margin-top: 4px;
  }
  .divider {
    width: 2px;
    height: 110px;
    background: var(--accent-blue);
  }
  .contact-list {
    list-style: none;
    display: flex;
    flex-direction: column;
    gap: 12px;
  }
  .contact-item {
    display: flex;
    align-items: center;
    gap: 12px;
    color: var(--text-light);
    font-size: 16px;
  }
  .contact-icon {
    width: 18px;
    height: 18px;
    flex: none;
  }
  .address {
    position: absolute;
    right: 70px;
    bottom: 60px;
    color: var(--text-muted);
    font-size: 16px;
    letter-spacing: 0.4px;
  }

  /* Front side: company name in place of the mark */
  .brand {
    position: absolute;
    inset: 0 0 12px 0;
    display: flex;
    align-items: center;
    justify-content: center;
    gap: 26px;
  }
  .brand-square {
    width: 44px;
    height: 44px;
    background: var(--brand-grey);
    flex: none;
  }
  .brand-name {
    color: var(--brand-grey);
    font-weight: 700;
    font-size: 58px;
    letter-spacing: 1px;
    white-space: nowrap;
  }
</style>
</head>
<body>
<main class="canvas">

  <section class="card card-back" aria-label="Business card back with contact details">
    <div class="contact-block">
      <div class="person">
        <p class="person-name">Daniel Reyes</p>
        <p class="person-title">President</p>
      </div>
      <div class="divider"></div>
      <ul class="contact-list">
        <li class="contact-item">
          <svg class="contact-icon" viewBox="0 0 24 24" aria-hidden="true">
            <path fill="var(--accent-blue)" d="M6.6 10.8c1.4 2.8 3.8 5.1 6.6 6.6l2.2-2.2c.3-.3.7-.4 1-.2 1.1.4 2.3.6 3.6.6.6 0 1 .4 1 1V20c0 .6-.4 1-1 1C10.6 21 3 13.4 3 4c0-.6.4-1 1-1h3.5c.6 0 1 .4 1 1 0 1.3.2 2.5.6 3.6.1.3 0 .7-.2 1l-2.3 2.2z"/>
          </svg>
          <span>+00 000 000 000</span>
        </li>
        <li class="contact-item">
          <svg class="contact-icon" viewBox="0 0 24 24" aria-hidden="true">
            <rect x="2.5" y="5" width="19" height="14" rx="1.5" fill="none" stroke="var(--accent-blue)" stroke-width="2"/>
            <path d="M3 6l9 7 9-7" fill="none" stroke="var(--accent-blue)" stroke-width="2"/>
          </svg>
          <span>info@rwframeworks.com</span>
        </li>
        <li class="contact-item">
          <svg class="contact-icon" viewBox="0 0 24 24" aria-hidden="true">
            <circle cx="12" cy="12" r="9" fill="none" stroke="var(--accent-blue)" stroke-width="2"/>
            <ellipse cx="12" cy="12" rx="4" ry="9" fill="none" stroke="var(--accent-blue)" stroke-width="1.6"/>
            <path d="M3 12h18" stroke="var(--accent-blue)" stroke-width="1.6"/>
          </svg>
          <span>www.rwframeworks.com</span>
        </li>
      </ul>
    </div>
    <p class="address">00000 Harbor Road, Unit 000, CA 00000</p>
  </section>

  <section class="card card-front" aria-label="Business card front with company name">
    <div class="brand">
      <span class="brand-square" aria-hidden="true"></span>
      <h1 class="brand-name">RW Frameworks Inc</h1>
    </div>
  </section>

</main>
</body>
</html>
```